Alderpoint Web Services

This is a new It services company operating in Perth western Australia

we need a website that is easy to navigate without a cluttered feel to it it should have the following links and pages

About Us
Services
Clients
Contact Us
MY Alderpoint (login for clients)

Hi it is a web based IT services company so we would expect customers to come to the website for 2 different purposes the first is to enquire about our services and then as they become customers come to our website to manage their services so whilst they are seperate we want do not want it to look like 2 different websites

hope this helps

Hi to update this we need a home page and templates for sub pages

this is a design brief only and not the coding of the pages or building of the site

```html
<!DOCTYPE html>
<html lang="en">
<head>
<meta charset="utf-8">
<title>Alderpoint Web Services</title>
<link rel="stylesheet" href="https://fonts.googleapis.com/css2?family=Orbitron:wght@600;700&family=Arimo:wght@400;700&family=Open+Sans:wght@400;600&display=swap">
<style>
:root{
  --red:#d40000;
  --red-dark:#9b0000;
  --red-deep:#a60a0a;
  --blue-band:rgba(27,66,112,0.94);
  --logo-blue:#1d3c8c;
  --grey-text:#555;
  --grey-light:#8a8a8a;
  --white:#fff;
  --pink-text:#f2b3b3;
}
*{box-sizing:border-box;margin:0;padding:0}
html,body{width:1050px;height:1200px;overflow:hidden;background:var(--white)}
body{position:relative;font-family:"Arimo",Arial,sans-serif;color:var(--grey-text)}
.abs{position:absolute}

/* header */
.site-header{left:0;top:0;width:1050px;height:80px;background:rgba(255,255,255,0.94);z-index:3}
.brand{left:150px;top:14px;display:flex;align-items:center;gap:12px}
.brand-dot{width:54px;height:54px;border-radius:50%;background:var(--red)}
.brand-name{font-family:"Orbitron",sans-serif;font-weight:700;font-size:27px;color:var(--logo-blue);letter-spacing:1px}
.utility{right:148px;top:11px;display:flex;gap:14px;font-family:"Open Sans",sans-serif;font-size:8px;color:#666;align-items:center}
.utility .lang{font-weight:600;color:#444}
.utility .phone{font-weight:600;color:#444;margin-left:8px}
.main-nav{left:531px;top:43px;display:flex;gap:15px;font-family:"Open Sans",sans-serif;font-size:12px;color:#555}
.btn-account{left:780px;top:34px;width:121px;height:35px;border-radius:2px;background:linear-gradient(#f00 0%,var(--red) 60%,#b00000 100%);color:var(--white);font-family:"Orbitron",sans-serif;font-size:8.5px;font-weight:700;display:flex;align-items:center;justify-content:center;gap:4px;box-shadow:0 1px 2px rgba(0,0,0,.3)}

/* hero */
.hero-visual{left:0;top:80px;width:1050px;height:548px;background:linear-gradient(110deg,#a9404e 0%,#e7c2cd 30%,#f1dbe2 50%,#c78a99 70%,#ead3dc 100%)}
.intro-band{left:0;top:330px;width:1050px;height:145px;background:var(--blue-band)}
.band-title{font-family:"Orbitron",sans-serif;font-weight:700;font-size:18px;color:var(--white);letter-spacing:1px}
.intro-title{left:161px;top:345px}
.intro-text{left:161px;top:379px;width:472px;font-size:10.6px;line-height:12.6px;color:var(--white)}
.login-title{left:682px;top:345px}
.login-field{left:684px;width:192px;height:26px;background:#eef1f4;border:1px solid #c9d0d8;font-size:11px;color:#333;padding:7px 9px}
.remember{left:684px;top:444px;display:flex;align-items:center;gap:5px;font-size:9px;color:var(--white)}
.remember span.box{width:13px;height:13px;background:#eee;border:1px solid #ccc}
.btn-login{left:787px;top:437px;width:89px;height:26px;background:linear-gradient(#e80000,#b40000);color:var(--white);font-family:"Orbitron",sans-serif;font-weight:700;font-size:8.5px;display:flex;align-items:center;justify-content:center}

/* services */
.services-title{left:0;width:1050px;top:505px;text-align:center}
.services-rule{left:195px;top:533px;width:660px;height:1px;background:rgba(255,255,255,.6)}
.slider-arrow{top:606px;width:44px;height:44px;border-radius:50%;display:flex;align-items:center;justify-content:center}
.slider-prev{left:127px;background:rgba(255,255,255,.35)}
.slider-next{left:880px;background:rgba(170,30,30,.75)}
.service-card-raised{left:358px;top:628px;width:166px;height:160px;background:var(--white);box-shadow:0 1px 6px rgba(0,0,0,.22)}
.service-icon{width:118px;height:118px;border-radius:50%;background:var(--white);top:551px;display:flex;align-items:center;justify-content:center}
.service-name{width:150px;text-align:center;font-family:"Orbitron",sans-serif;font-weight:700;font-size:9px;line-height:14px;color:var(--red-deep);letter-spacing:.5px}
.service-text{width:150px;text-align:center;font-size:10.6px;line-height:12.6px;color:#333}
.btn-more{left:387px;top:746px;width:108px;height:26px;border:1px solid #ddd;box-shadow:0 1px 3px rgba(0,0,0,.15);font-family:"Orbitron",sans-serif;font-weight:700;font-size:8.5px;color:var(--red-deep);display:flex;align-items:center;justify-content:center}

/* call to action */
.cta-band{left:0;top:816px;width:1050px;height:302px;background:var(--red-dark)}
.cta-illustration{left:178px;top:820px;width:318px;height:298px;border-radius:50% 50% 44% 44%;background:radial-gradient(circle,#d79a9a 0%,#b94848 55%,var(--red-dark) 100%)}
.cta-title{left:520px;top:879px;width:350px;text-align:center;font-family:"Orbitron",sans-serif;font-weight:700;font-size:17px;line-height:27px;color:var(--white);letter-spacing:1.5px}
.cta-text{left:530px;top:968px;width:330px;text-align:center;font-size:10.6px;line-height:13px;color:var(--pink-text)}
.btn-cta{top:1015px;width:121px;height:33px;background:linear-gradient(#f00,#c00000);color:var(--white);font-family:"Orbitron",sans-serif;font-weight:700;font-size:8.5px;display:flex;align-items:center;justify-content:center;gap:4px;box-shadow:0 1px 3px rgba(0,0,0,.35)}

/* footer */
.footer-brand{left:0;width:1050px;top:1132px;display:flex;justify-content:center;align-items:center;gap:5px}
.footer-brand .brand-dot{width:18px;height:18px}
.footer-brand .brand-name{font-size:10px}
.footer-links{left:0;width:1050px;top:1155px;text-align:center;font-size:8.6px;color:var(--grey-light);word-spacing:1px}
.footer-links .sep{margin:0 8px}
.social-list{left:0;width:1050px;top:1171px;display:flex;justify-content:center;gap:7px}
.social-list span{width:15px;height:15px;background:var(--red-deep);border-radius:2px}
</style>
</head>
<body>

<header class="site-header abs">
  <div class="brand abs" style="position:absolute"><span class="brand-dot"></span><span class="brand-name">Alderpoint</span></div>
  <div class="utility abs"><span>Login</span><span>Help</span><span>Cookies</span><span>Policy</span><span class="lang">English ▾</span><span class="phone">08-9555-0142</span>
    <svg width="9" height="9" viewBox="0 0 10 10"><path d="M2 1l2 2-1 1.5c.8 1.3 1.5 2 2.8 2.7L7.3 6l2 2-1.3 1.5C4.5 9 1 5.5.5 2z" fill="#999"/></svg></div>
  <nav class="main-nav abs"><span>About Us</span><span>Services</span><span>Clients</span><span>Contact Us</span></nav>
  <div class="btn-account abs">
    <svg width="8" height="8" viewBox="0 0 10 10"><circle cx="5" cy="3" r="2.4" fill="#fff"/><path d="M0.5 10c0-3 2-4.5 4.5-4.5S9.5 7 9.5 10z" fill="#fff"/></svg>MY Alderpoint</div>
</header>

<div class="hero-visual abs" role="img" aria-label="Photograph of a hand touching floating transparent cubes showing IT imagery, red-tinted"></div>

<section class="intro-band abs"></section>
<h1 class="band-title intro-title abs">WEB BASED IT SERVICES</h1>
<p class="intro-text abs">Lorem ipsum dolor sit amet, consectetuer adipiscing elit, sed diam nonummy nibh euismod tincidunt ut laoreet dolore magna aliquam erat volutpat. Ut wisi enim ad minim veniam, quis nostrud exerci tation ullamcorper suscipit lobortis nisl ut aliquip ex ea commodo consequat. Duis autem vel eum iriure dolor in hendrerit in vulputate velit esse molestie consequat, vel illum dolore eu feugiat nulla facilisis at vero eros et accumsan et iusto odio dignissim qui blandit praesent luptatum zzril delenit augue duis dolore te feugait nulla facilisi.</p>
<h2 class="band-title login-title abs">CUSTOMER LOGIN</h2>
<div class="login-field abs" style="top:380px">Username</div>
<div class="login-field abs" style="top:408px">Password</div>
<div class="remember abs"><span class="box"></span>Save Password</div>
<div class="btn-login abs">LOGIN</div>

<h2 class="band-title services-title abs">OUR SERVICES</h2>
<div class="services-rule abs"></div>
<div class="slider-arrow slider-prev abs"><svg width="14" height="22" viewBox="0 0 14 22"><path d="M11 2L3 11l8 9" stroke="#888" stroke-width="1.5" fill="none"/></svg></div>
<div class="slider-arrow slider-next abs"><svg width="14" height="22" viewBox="0 0 14 22"><path d="M3 2l8 9-8 9" stroke="#5a0000" stroke-width="1.5" fill="none"/></svg></div>

<div class="service-card-raised abs"></div>

<div class="service-icon abs" style="left:209px"><svg width="44" height="48" viewBox="0 0 44 48"><circle cx="22" cy="14" r="10" fill="#b30000"/><path d="M10 15a12 12 0 0124 0" stroke="#b30000" stroke-width="3" fill="none"/><path d="M4 48c0-12 8-18 18-18s18 6 18 18z" fill="#b30000"/></svg></div>
<div class="service-icon abs" style="left:382px"><svg width="46" height="46" viewBox="0 0 46 46"><circle cx="23" cy="23" r="19" fill="none" stroke="#b30000" stroke-width="6" stroke-dasharray="5 4"/><circle cx="23" cy="23" r="14" fill="#b30000"/><path d="M9 23h28M23 9v28M13 16h20M13 30h20" stroke="#fff" stroke-width="1.3"/><ellipse cx="23" cy="23" rx="6" ry="14" stroke="#fff" stroke-width="1.3" fill="none"/></svg></div>
<div class="service-icon abs" style="left:551px"><svg width="46" height="46" viewBox="0 0 46 46"><rect x="4" y="14" width="38" height="24" rx="2" fill="none" stroke="#b30000" stroke-width="3"/><path d="M17 44h12M23 38v6" stroke="#b30000" stroke-width="3"/><rect x="14" y="2" width="14" height="22" rx="2" fill="#b30000"/><rect x="30" y="8" width="10" height="16" rx="1" fill="#b30000"/></svg></div>
<div class="service-icon abs" style="left:722px"><svg width="44" height="46" viewBox="0 0 44 46"><circle cx="14" cy="7" r="6" fill="#b30000"/><path d="M4 46V22c0-6 4-9 10-9s10 3 10 9v24z" fill="#b30000"/><circle cx="30" cy="30" r="9" fill="none" stroke="#b30000" stroke-width="5" stroke-dasharray="3.5 2.5"/><circle cx="30" cy="30" r="5" fill="#b30000"/><circle cx="30" cy="30" r="2" fill="#fff"/></svg></div>

<h3 class="service-name abs" style="left:193px;top:636px">CUSTOMER<br>SUPPORT</h3>
<h3 class="service-name abs" style="left:366px;top:638px">APPLICATION<br>DEVELOPMENT</h3>
<h3 class="service-name abs" style="left:535px;top:638px">APPLICATION<br>MANAGEMENT</h3>
<h3 class="service-name abs" style="left:706px;top:638px">BUSINESS AND<br>IT CONSULTING</h3>

<p class="service-text abs" style="left:193px;top:675px">Ut wisi enim ad minim veniam, quis nostrud exerci tation ullamcorper suscipit lobortis nisl ut aliquip ex ea commodo consequat.</p>
<p class="service-text abs" style="left:366px;top:675px">Lorem ipsum dolor sit amet, consectetuer adipiscing elit, sed diam nonummy nibh euismod tincidunt ut laoreet dolore magna…</p>
<p class="service-text abs" style="left:535px;top:675px">Duis autem vel eum iriure dolor in hendrerit in vulputate velit esse molestie consequat, vel illum dolore eu feugiat nulla …</p>
<p class="service-text abs" style="left:706px;top:675px">Facilisis at vero eros et accumsan et iusto odio dignissim qui blandit praesent luptatum zzril delenit augue duis dolore te feugait nulla facilisi.</p>
<div class="btn-more abs">read more ››</div>

<section class="cta-band abs"></section>
<div class="cta-illustration abs" role="img" aria-label="Illustration of a tree made of arrows and small technology icons in white on red"></div>
<h2 class="cta-title abs">THIS COULD BE THE BEGINNING OF A SUCCESSFUL BUSINESS .</h2>
<p class="cta-text abs">Duis autem vel eum iriure dolor in hendrerit in vulputate velit esse molestie consequat, vel illum dolore eu feugiat nulla …</p>
<div class="btn-cta abs" style="left:575px"><svg width="11" height="10" viewBox="0 0 11 10"><circle cx="4" cy="3" r="2.5" fill="#fff"/><path d="M0 10c0-3 2-4.5 4-4.5S8 7 8 10z" fill="#fff"/><path d="M7 6l4-3" stroke="#fff" stroke-width="1.5"/></svg>SIGN UP</div>
<div class="btn-cta abs" style="left:703px"><svg width="12" height="9" viewBox="0 0 12 9"><rect width="12" height="9" fill="#fff"/><path d="M0 0l6 5 6-5" stroke="#c00000" stroke-width="1.2" fill="none"/></svg>CONTACT</div>

<footer>
  <div class="footer-brand abs"><span class="brand-dot"></span><span class="brand-name">Alderpoint</span></div>
  <p class="footer-links abs">Privacy Policy<span class="sep">|</span>Terms &amp; Conditions<span class="sep">|</span>Alderpoint Pty Ltd - 42 Kings Park Rd, Level 3 - West Perth - WA 6005 - Australia © Alderpoint 2014</p>
  <div class="social-list abs"><span></span><span></span><span></span><span></span><span></span><span></span></div>
</footer>

</body>
</html>
```